the look of import selling star-up company

I have attached rhino logo that i like (can be edit) and i wanna turn that in to luxury look. Example like black base and gold logo +luxury looking font.

Company name: Vantel trading Oy
Slogan: Setting a higher standard.
CEO Jarmo Keskinen
Starting to import ceramic nano coatings to cars, in home use and industrial purposes.

Target Market(s)

30-60 year old men and women ho have big money and know what car they drive

Industry/Entity Type

It Company

```html
<!DOCTYPE html>
<html lang="en">
<head>
<meta charset="utf-8">
<title>Vantel trading Oy – Business Cards</title>
<link rel="stylesheet" href="https://fonts.googleapis.com/css2?family=Marcellus&family=Montserrat:wght@400;600;700&display=swap">
<style>
  :root {
    --backdrop: #dcdcde;
    --card-black: #0b0b0b;
    --gold: #d8a92a;
    --gold-light: #f3d36a;
    --gold-deep: #a97a12;
    --white: #ffffff;
    --name-grey: #d9d9d9;
    --muted: #8c8c8c;
  }
  * { box-sizing: border-box; margin: 0; padding: 0; }
  html, body {
    width: 1200px;
    height: 1000px;
    overflow: hidden;
    background: var(--backdrop);
  }
  .canvas {
    position: relative;
    width: 1200px;
    height: 1000px;
  }
  .card {
    position: absolute;
    width: 560px;
    height: 320px;
    border-radius: 22px;
    background: var(--card-black);
    overflow: hidden;
    box-shadow: 0 18px 40px rgba(0,0,0,0.25);
  }

  /* Contact side */
  .card--contact { left: 80px; top: 90px; }
  .gold-band {
    position: absolute;
    left: 0;
    height: 7px;
    width: 290px;
    background: linear-gradient(90deg, var(--gold-deep), var(--gold-light) 45%, var(--gold) 70%, var(--gold-deep));
  }
  .gold-band--top { top: 34px; }
  .gold-band--bottom { bottom: 34px; }
  .contact-block {
    position: absolute;
    left: 42px;
    top: 84px;
    font-family: 'Montserrat', sans-serif;
    color: var(--white);
  }
  .person-name {
    font-weight: 700;
    font-size: 20px;
    letter-spacing: 1.5px;
    font-variant: small-caps;
  }
  .person-role {
    font-weight: 700;
    font-size: 17px;
    color: var(--gold);
    margin-top: 2px;
    margin-bottom: 14px;
  }
  .contact-group { margin-bottom: 12px; }
  .contact-line {
    display: grid;
    grid-template-columns: 46px 1fr;
    font-size: 12.5px;
    line-height: 17px;
  }
  .contact-label { font-weight: 700; }
  .contact-value { font-weight: 400; }
  .brand-mark {
    position: absolute;
    right: 58px;
    top: 62px;
    width: 170px;
    text-align: center;
  }
  .brand-mark__circle {
    width: 150px;
    height: 150px;
    border-radius: 50%;
    background: var(--white);
    margin: 0 auto 14px;
  }
  .brand-mark__name {
    font-family: 'Montserrat', sans-serif;
    font-weight: 600;
    font-size: 14px;
    letter-spacing: 1px;
    color: var(--white);
  }

  /* Brand side */
  .card--brand { left: 560px; top: 560px; }
  .gold-frame {
    position: absolute;
    inset: 16px;
    border: 1.5px solid var(--gold-deep);
    border-radius: 12px;
  }
  .brand-emblem {
    position: absolute;
    left: 50%;
    top: 48px;
    width: 150px;
    height: 150px;
    margin-left: -75px;
    border-radius: 50%;
    background: var(--gold);
  }
  .brand-name {
    position: absolute;
    left: 0; right: 0;
    top: 214px;
    text-align: center;
    font-family: 'Marcellus', serif;
    font-size: 30px;
    letter-spacing: 2px;
    color: var(--name-grey);
  }
  .brand-slogan {
    position: absolute;
    left: 0; right: 0;
    top: 254px;
    text-align: center;
    font-family: 'Marcellus', serif;
    font-size: 13px;
    letter-spacing: 2.5px;
    color: var(--muted);
  }
</style>
</head>
<body>
<main class="canvas">

  <section class="card card--contact" aria-label="Business card, contact side">
    <div class="gold-band gold-band--top"></div>
    <div class="gold-band gold-band--bottom"></div>

    <div class="contact-block">
      <p class="person-name">Jarmo Keskinen</p>
      <p class="person-role">CEO</p>

      <div class="contact-group">
        <p class="contact-line"><span class="contact-label">Call</span><span class="contact-value">- 040-7712-358</span></p>
        <p class="contact-line"><span class="contact-label">Fax</span><span class="contact-value">- 040-7712-359</span></p>
      </div>
      <div class="contact-group">
        <p class="contact-line"><span class="contact-label">Web</span><span class="contact-value">- www.vanteltradingoy.com</span></p>
        <p class="contact-line"><span class="contact-label">Mail</span><span class="contact-value">- vanteltradingoy.com</span></p>
      </div>
      <div class="contact-group">
        <p class="contact-line"><span class="contact-label">Add</span><span class="contact-value">- 4th floor, Harbour Street,<br>&nbsp;&nbsp;Lakeview-4120</span></p>
      </div>
    </div>

    <div class="brand-mark">
      <div class="brand-mark__circle"></div>
      <p class="brand-mark__name">Vantel trading Oy</p>
    </div>
  </section>

  <section class="card card--brand" aria-label="Business card, brand side">
    <div class="gold-frame"></div>
    <div class="brand-emblem"></div>
    <p class="brand-name">VANTEL TRADING OY</p>
    <p class="brand-slogan">SETTING A HIGHER STANDARD</p>
  </section>

</main>
</body>
</html>
```